Monument sign* - Law Firm

*I am installing a monument sign that has LED, as well as backlit elements. I am seeking help in designing the backlit portion of the sign. The Backlit sign will be 12’ x 4’.

We are looking for a classic, yet eye-catching sign to help new and current clients find our firm as well as bring in future clients. One of our goals is that people who drive by on a regular basis remember our sign (and us) for any future legal need.

Target Market(s)

Current and future clientele

Industry/Entity Type

Law Firm

Font styles to use
Serif
Sans Serif

Colors
b1b1b1
333333

Requirements
Must have
• Business name: Hargrove Law Firm, Inc.
• Website: www.hargrovelawfirm-example.com
• Telephone: (555)214-3679
• Our firm's logo
Nice to have
• Color preference is black, taupe, and white. A photo for reference of the office coloring is uploaded.
• We currently have an established logo which our firm has been using for more than 10 years. Our logo has been used in advertising, commercials, letterhead, and on-site. We are looking to transition from brown/rust/cream to the black/taupe/white color scheme.
Should not have
• Cheesy slogans; character designs; directions; additional symbols outside of the firm's logo.

```html
<!DOCTYPE html>
<html lang="en">
<head>
<meta charset="UTF-8">
<title>Hargrove Law Firm, Inc. — Monument Sign</title>
<link rel="stylesheet" href="https://fonts.googleapis.com/css2?family=Oswald:wght@400&display=swap">
<style>
  :root {
    --page: #ffffff;
    --taupe-grey: #b1b1b1;
    --charcoal: #333333;
  }
  html, body {
    margin: 0;
    padding: 0;
    background: var(--page);
    overflow: hidden;
  }
  .canvas {
    position: relative;
    width: 1200px;
    height: 540px;
    background: var(--page);
    overflow: hidden;
  }
  .sign-face {
    position: absolute;
    left: 32px;
    top: 44px;
    width: 1134px;
    height: 450px;
    background: var(--taupe-grey);
    overflow: hidden;
  }
  .brand-mark {
    position: absolute;
    left: 30px;
    top: 33px;
    width: 240px;
    height: 389px;
    display: flex;
    flex-direction: column;
    align-items: center;
    justify-content: center;
    gap: 18px;
  }
  .brand-mark__square {
    width: 236px;
    height: 236px;
    background: var(--charcoal);
  }
  .brand-mark__name {
    font-family: "Oswald", sans-serif;
    font-weight: 400;
    font-size: 68px;
    line-height: 1;
    color: var(--charcoal);
    letter-spacing: 0.5px;
    white-space: nowrap;
  }
  .firm-name {
    position: absolute;
    left: 444px;
    top: 116px;
    margin: 0;
    font-family: "Oswald", sans-serif;
    font-weight: 400;
    font-size: 78px;
    line-height: 1;
    color: var(--charcoal);
    letter-spacing: -1px;
    white-space: nowrap;
  }
  .contact {
    position: absolute;
    left: 598px;
    top: 268px;
    margin: 0;
    padding: 0;
    list-style: none;
    font-family: "Oswald", sans-serif;
    font-weight: 400;
    font-size: 32px;
    line-height: 1;
    color: var(--charcoal);
  }
  .contact__item {
    display: flex;
    align-items: center;
    gap: 10px;
    height: 50px;
    margin-bottom: 3px;
    white-space: nowrap;
  }
  .contact__icon {
    width: 28px;
    height: 28px;
    flex: none;
  }
</style>
</head>
<body>
  <div class="canvas">
    <div class="sign-face">
      <div class="brand-mark">
        <div class="brand-mark__square"></div>
        <div class="brand-mark__name">Hargrove</div>
      </div>

      <h1 class="firm-name">Hargrove Law Firm, Inc.</h1>

      <ul class="contact">
        <li class="contact__item">
          <svg class="contact__icon" viewBox="0 0 24 24" fill="none" stroke="#333333" stroke-width="1.6" aria-hidden="true">
            <circle cx="12" cy="12" r="10"/>
            <ellipse cx="12" cy="12" rx="4.2" ry="10"/>
            <line x1="2" y1="12" x2="22" y2="12"/>
            <path d="M4 6.5h16M4 17.5h16"/>
          </svg>
          <span class="contact__text">www.hargrovelawfirm-example.com</span>
        </li>
        <li class="contact__item">
          <svg class="contact__icon" viewBox="0 0 24 24" fill="none" stroke="#333333" stroke-width="1.6" stroke-linecap="round" stroke-linejoin="round" aria-hidden="true">
            <path d="M6.5 3.5l3 4-2 2c1 2.4 3 4.4 5.5 5.5l2-2 4 3-1.8 2.6c-.5.7-1.4 1-2.2.7C9.6 17.4 6.6 14.4 4.2 9c-.3-.8 0-1.7.7-2.2z"/>
            <path d="M14 3.5a7 7 0 0 1 6.5 6.5M14 7a3.5 3.5 0 0 1 3 3"/>
          </svg>
          <span class="contact__text">(555)214-3679</span>
        </li>
      </ul>
    </div>
  </div>
</body>
</html>
```